Baby Care Print Log for Nannies and Parents- Creating a brand/style I can use across different forms

I am creating a notebook for babysitters to use to communicate with parents about the children they care for. I will be creating many different forms (emergency contacts, daily logs, shopping lists, etc.)
I need a look and feel from which to style these forms from. I am starting by designing the daily baby care log. I need a designer to take my Word doc with just text on it, and create a visual approach to make this visually appealing.
I do not want this to be extremely "babyish" with cartoon styling. I want it to be more of a professional looking style. I would like to be able to color each different document a different color palette, yet keep the similar look and feel. My logo is attached for inspiration. I use real photography across my website plumhollowkit.com.
Updates
I will be re-designing my Wordpress website based on what design I like best and also will need other forms completed once I pick a design. I am hoping to work with someone who I can hire for further development needs as well. Added Saturday, February 11, 2017
Target Market(s)
Professional Parents
Industry/Entity Type
Education
Requirements
Must have
- color, pop, visual appeal
- Please use the color in my logo and any complementary colors that you think work well with it. I definitely like colored patterns, ombre, colored backgrounds, etc. I'd prefer for it not to be completely white with only pops of color here and there.
Nice to have
- My logo somewhere subtly on the form
- Photography elements
Should not have
- cartoon images of babies, etc. I use real photography across my website with the exception of my logo umbrella.

```html
<!DOCTYPE html>
<html lang="en">
<head>
<meta charset="utf-8">
<title>Plum Hollow Kit – Daily Log</title>
<link href="https://fonts.googleapis.com/css2?family=Open+Sans:wght@400;600;700&family=Nothing+You+Could+Do&display=swap" rel="stylesheet">
<style>
  :root{
    --paper:#fbfbfa;
    --ink:#2b2b2b;
    --hand:#1f1f24;
    --pink:#e0457b;
    --blue:#3d7cc9;
    --orange:#ef7b3f;
    --yellow:#f2c040;
    --teal:#2f8f93;
    --red:#e35b4f;
    --label:#c55a2c;
    --rule:#d9d4cf;
  }
  *{box-sizing:border-box;margin:0;padding:0}
  html,body{width:898px;height:1200px;overflow:hidden;background:var(--paper)}
  body{position:relative;font-family:"Open Sans",Arial,sans-serif;color:var(--ink)}
  .hand{font-family:"Nothing You Could Do",cursive;color:var(--hand)}
  .family-tag{position:absolute;left:540px;top:48px;width:310px;height:46px;background:var(--blue);color:#fff;font-size:15px;font-weight:600;letter-spacing:1px;display:flex;align-items:center;justify-content:center;text-transform:uppercase}
  .brand{position:absolute;left:70px;top:95px;display:flex;align-items:center;gap:18px}
  .brand-dot{width:40px;height:40px;border-radius:50%;background:var(--blue)}
  .brand-name{font-size:50px;font-weight:700;color:var(--ink);letter-spacing:-.5px}
  .rule-pink{position:absolute;left:50px;width:798px;height:3px;background:var(--pink)}
  .photo{position:absolute;left:50px;top:200px;width:798px;height:440px;background:linear-gradient(135deg,#8fb35a 0%,#5e8f3c 45%,#e8a43c 62%,#d9493e 78%,#6a9b47 100%)}
  .child-tag{position:absolute;left:75px;top:570px;width:380px;height:48px;background:#fff;display:flex;align-items:center;font-size:26px}
  .child-tag span{padding:0 22px}
  .child-tag .date{border-left:2px solid var(--rule);margin-left:auto}
  .activities{position:absolute;left:560px;top:218px;width:270px;height:400px;background:#fff;border:4px solid var(--red);border-radius:10px;padding:18px 18px}
  .box-title{font-size:12px;font-weight:700;letter-spacing:1px;text-transform:uppercase;text-align:center;color:var(--label)}
  .activities p{margin-top:14px;font-size:25px;line-height:34px}
  .card{position:absolute;background:#fff;border-radius:10px;padding:14px 14px}
  .naps-a{left:55px;top:665px;width:215px;height:235px;border:4px solid var(--orange)}
  .naps-b{left:290px;top:665px;width:215px;height:235px;border:4px solid var(--yellow)}
  .feeding{left:545px;top:700px;width:305px;height:230px;border:4px solid var(--orange)}
  .cols{display:grid;margin-top:10px;font-size:10px;color:var(--label);text-transform:uppercase}
  .cols.two{grid-template-columns:1fr 1fr}
  .cols.four{grid-template-columns:.9fr 1.1fr 1fr 1fr}
  .rows{position:relative}
  .row{display:grid;border-bottom:1px solid var(--rule);height:30px;align-items:end;font-size:20px;white-space:nowrap}
  .rows.two .row{grid-template-columns:1fr 1fr}
  .rows.four .row{grid-template-columns:.9fr 1.1fr 1fr 1fr;height:26px;font-size:19px}
  .split{position:absolute;left:50%;top:0;bottom:0;width:1px;background:var(--ink)}
  .mood{position:absolute;left:62px;top:925px;width:345px;height:48px;border:4px solid var(--teal);border-radius:10px;display:flex;align-items:center;padding-left:14px;background:#fff}
  .mood b{font-size:13px;letter-spacing:1px;color:var(--teal)}
  .mood .hand{font-size:24px;margin-left:6px}
  .notes{position:absolute;top:1015px;font-size:13px;font-weight:700;letter-spacing:1px;color:var(--blue);text-transform:uppercase}
  .notes-special{left:62px;width:380px}
  .notes-groceries{left:500px;width:340px}
  .notes p{margin-top:6px;font-size:25px;line-height:32px;letter-spacing:0;text-transform:none;font-weight:400;overflow-wrap:break-word}
  .divider{position:absolute;left:470px;top:1020px;width:1px;height:90px;background:var(--rule)}
</style>
</head>
<body>
  <div class="family-tag">The Lawson Family</div>
  <div class="brand"><div class="brand-dot"></div><div class="brand-name">Plum Hollow Kit</div></div>
  <div class="rule-pink" style="top:186px"></div>

  <div class="photo" role="img" aria-label="Photograph of a child holding a rainbow umbrella on green grass"></div>
  <div class="child-tag hand"><span>Milo</span><span class="date">2/15/17</span></div>

  <div class="activities">
    <div class="box-title">Today's Activities</div>
    <p class="hand">We had a great day! We saw Mrs. Bennett at the park. We went for a long walk and ate lunch in the back yard. I'll see you early tomorrow at 7:30.</p>
  </div>

  <div class="card naps-a">
    <div class="box-title">Naps</div>
    <div class="cols two"><span>Time</span><span>Length</span></div>
    <div class="rows two hand">
      <div class="split"></div>
      <div class="row"><span>10:00</span><span>&nbsp;1 hour</span></div>
      <div class="row"><span>1:30</span><span>&nbsp;2 hours</span></div>
      <div class="row"><span></span><span></span></div>
      <div class="row"><span></span><span></span></div>
    </div>
  </div>

  <div class="card naps-b">
    <div class="box-title">Naps</div>
    <div class="cols two"><span>Wet</span><span>BM</span></div>
    <div class="rows two hand">
      <div class="split"></div>
      <div class="row"><span>8:00am</span><span>&nbsp;10:00am</span></div>
      <div class="row"><span>10:00am</span><span></span></div>
      <div class="row"><span>1:00pm</span><span></span></div>
      <div class="row"><span>3:00pm</span><span>&nbsp;4:00pm</span></div>
    </div>
  </div>

  <div class="card feeding">
    <div class="box-title">Feeding</div>
    <div class="cols four"><span>Time</span><span>Milk (oz)</span><span>Water</span><span>Food</span></div>
    <div class="rows four hand">
      <div class="row"><span>8:00</span><span>8oz</span><span></span><span></span></div>
      <div class="row"><span>10:00</span><span>8oz</span><span></span><span>Rice</span></div>
      <div class="row"><span>11:00</span><span></span><span>2oz</span><span></span></div>
      <div class="row"><span>1:00</span><span>8oz</span><span></span><span></span></div>
      <div class="row"><span>3:00</span><span>8oz</span><span></span><span></span></div>
    </div>
  </div>

  <div class="mood"><b>MOOD</b><span class="hand">Happy all day :)</span></div>

  <div class="rule-pink" style="top:995px"></div>
  <div class="notes notes-special">Special Notes<p class="hand">I brought in the milk off the front porch.</p></div>
  <div class="divider"></div>
  <div class="notes notes-groceries">Groceries<p class="hand">You are almost out of wipes.</p></div>
</body>
</html>
```